Corporate Business Card

Very professional, Modern, Not to busy, include phone address email, website
(555) 555-0174, 61807 19th Street N, Cedarmont, OR 98517, marcus@kestrelbayholding.com, brelvanindustries.com

Target Market(s)

Manufacturing

Industry/Entity Type

Aero, machining, manufacturing, Off road racing

Contact Information for Business Card

Phone, address email, website

```html
<!DOCTYPE html>
<html lang="en">
<head>
<meta charset="utf-8">
<title>Brelvan Industries – Business Card</title>
<link href="https://fonts.googleapis.com/css2?family=Archivo:wdth,wght@125,800&family=Poppins:wght@400;700&display=swap" rel="stylesheet">
<style>
  :root {
    --navy: #1b3a73;
    --navy-deep: #173366;
    --red: #d3222a;
    --paper: #ffffff;
    --stage: #ffffff;
  }
  * { margin: 0; padding: 0; box-sizing: border-box; }
  html, body { width: 1200px; height: 675px; overflow: hidden; }
  body { background: var(--stage); position: relative; font-family: 'Poppins', sans-serif; }

  .card {
    position: absolute; top: 179px; width: 493px; height: 288px; overflow: hidden;
    box-shadow: 0 4px 10px rgba(0,0,0,0.25);
  }
  .card-front {
    left: 88px;
    background: linear-gradient(135deg, #e9e9ea 0%, #f7f7f7 35%, var(--paper) 60%);
  }
  .card-back { left: 624px; background: var(--navy); }

  .brand-name {
    position: absolute; left: 32px; top: 46px;
    font-family: 'Poppins', sans-serif; font-weight: 700;
    font-size: 32px; line-height: 1; color: var(--navy); letter-spacing: 0.2px;
  }

  .holder-name {
    position: absolute; left: 32px; top: 161px;
    font-family: 'Archivo', sans-serif; font-weight: 800; font-stretch: 125%;
    font-size: 16.5px; color: var(--navy); letter-spacing: 0.3px;
  }
  .holder-title {
    position: absolute; left: 32px; top: 183px;
    font-family: 'Archivo', sans-serif; font-weight: 800; font-stretch: 125%;
    font-size: 11px; color: var(--red);
  }
  .title-rule {
    position: absolute; left: 141px; right: 31px; top: 193px;
    height: 1.5px; background: var(--navy);
  }

  .contact-list { position: absolute; left: 32px; top: 205px; list-style: none; }
  .contact-list li {
    display: flex; align-items: center; gap: 9px;
    height: 16.5px; font-size: 12.5px; color: var(--navy);
  }
  .contact-list svg { width: 10px; height: 10px; fill: var(--red); flex: none; }

  .address {
    position: absolute; right: 31px; top: 203px;
    font-size: 11.5px; color: var(--navy);
  }

  .base-bands { position: absolute; left: 0; bottom: 0; width: 493px; height: 19px; }

  .back-pattern { position: absolute; inset: 0; background: var(--navy-deep); }
  .back-brand {
    position: absolute; left: 352px; top: 238px;
    font-family: 'Poppins', sans-serif; font-weight: 700;
    font-size: 14px; color: var(--paper);
  }
</style>
</head>
<body>

<section class="card card-front" aria-label="Business card front">
  <div class="brand-name">Brelvan Industries</div>

  <div class="holder-name">DANIEL WHITCOMB</div>
  <div class="holder-title">CEO/FOUNDER</div>
  <div class="title-rule"></div>

  <ul class="contact-list">
    <li>
      <svg viewBox="0 0 24 24" aria-hidden="true"><path d="M6.6 10.8a15.2 15.2 0 0 0 6.6 6.6l2.2-2.2c.3-.3.7-.4 1-.2 1.1.4 2.3.6 3.6.6.6 0 1 .4 1 1V20c0 .6-.4 1-1 1A17 17 0 0 1 3 4c0-.6.4-1 1-1h3.5c.6 0 1 .4 1 1 0 1.3.2 2.5.6 3.6.1.3 0 .7-.2 1z"/></svg>
      (555) 555-0174
    </li>
    <li>
      <svg viewBox="0 0 24 24" aria-hidden="true"><path d="M2 5h20v14H2z M2 5l10 7 10-7" stroke="#fff" stroke-width="1.6"/></svg>
      marcus@kestrelbayholding.com
    </li>
    <li>
      <svg viewBox="0 0 24 24" aria-hidden="true"><path d="M12 2a10 10 0 1 0 0 20 10 10 0 0 0 0-20zm0 2c.9 0 2.2 2 2.7 5H9.3C9.8 6 11.1 4 12 4zM4.3 9h3c-.1 1-.1 2 0 3h-3a8 8 0 0 1 0-3zm.6 5h2.6c.3 1.8.9 3.3 1.6 4.4A8 8 0 0 1 4.9 14zm4.4 0h5.4c-.5 3-1.8 6-2.7 6s-2.2-3-2.7-6zm0-2c-.1-1-.1-2 0-3h5.4c.1 1 .1 2 0 3zm7.2 2h2.6a8 8 0 0 1-4.2 4.4c.7-1.1 1.3-2.6 1.6-4.4zm.2-2c.1-1 .1-2 0-3h3a8 8 0 0 1 0 3z"/></svg>
      brelvanindustries.com
    </li>
  </ul>

  <div class="address">61807 19th Street N, Cedarmont, OR 98517</div>

  <svg class="base-bands" viewBox="0 0 493 19" aria-hidden="true">
    <rect x="0" y="8" width="254" height="11" fill="#1b3a73"/>
    <polygon points="260,19 272,0 493,0 493,19" fill="#d3222a"/>
  </svg>
</section>

<section class="card card-back" aria-label="Business card back">
  <div class="back-pattern" role="img" aria-label="Repeating tonal brand pattern on navy"></div>
  <div class="back-brand">Brelvan Industries</div>
</section>

</body>
</html>
```